Swimming Pool Business Billboard

10' x 24' Billboard displaying company name, logo and phone number. Picture of swimming pool activity; kids playing , swimming, etc. Bullet points possibly shown: New Construction, Repairs, Weekly maintenance.

Industry/Entity Type

Swimming pool construction, repairs and maintenance.

Font styles to use
Sans Serif

Colors
0054AA
0677BA
7BADD7
CADEEF
E8F1F8

Requirements
Must have
• Rusty & Calder Pembrook, RUSTY'S POOLS & Service,
Nice to have
• Prefer to have my last name "Pembrook" above the word "POOLS" only in smaller print so that "RUSTYS POOLS" is distinguished.

```html
<!DOCTYPE html>
<html lang="en">
<head>
<meta charset="utf-8">
<title>Rusty's Pools &amp; Service Billboard</title>
<link rel="stylesheet" href="https://fonts.googleapis.com/css2?family=Arvo:wght@400;700&display=swap">
<style>
  :root {
    --navy: #0f3f78;
    --brand-blue: #0054AA;
    --mid-blue: #0677BA;
    --soft-blue: #7BADD7;
    --pale-blue: #CADEEF;
    --mist: #E8F1F8;
    --page: #f4f6f9;
    --white: #ffffff;
    --pool: #3fd0dc;
    --pool-deep: #1aa7c4;
    --foliage: #4f7a3a;
    --sky: #7cc0e6;
  }
  * { box-sizing: border-box; margin: 0; padding: 0; }
  html, body { width: 998px; height: 1200px; overflow: hidden; }
  body {
    background: var(--page);
    font-family: "Arvo", "Rockwell", serif;
    color: var(--navy);
    position: relative;
  }
  .billboard {
    position: absolute;
    left: 49px; top: 412px;
    width: 900px; height: 375px;
    background: var(--white);
    overflow: hidden;
    box-shadow: 0 3px 10px rgba(0, 0, 0, 0.18);
  }
  .pool-photo {
    position: absolute;
    top: 0; right: 0;
    width: 560px; height: 100%;
    background:
      linear-gradient(180deg, var(--sky) 0%, var(--foliage) 22%, #8fb36a 40%, var(--pool) 58%, var(--pool-deep) 100%);
  }
  .photo-fade {
    position: absolute;
    top: 0; right: 0;
    width: 560px; height: 100%;
    background: linear-gradient(90deg, var(--white) 0%, rgba(255,255,255,0.85) 25%, rgba(255,255,255,0) 58%);
  }
  .frame {
    position: absolute;
    inset: 11px;
    border: 2px solid transparent;
    border-image: linear-gradient(90deg, var(--navy) 0%, var(--navy) 55%, rgba(15,63,120,0.25) 75%, rgba(15,63,120,0) 100%) 1;
  }
  .brand {
    position: absolute;
    left: 30px; top: 48px;
    display: flex; align-items: center; gap: 14px;
  }
  .brand-mark {
    width: 100px; height: 100px;
    border-radius: 50%;
    background: var(--brand-blue);
  }
  .brand-name {
    font-weight: 700;
    color: var(--navy);
    width: 342px;
  }
  .brand-owners {
    font-size: 16px;
    letter-spacing: 2.6px;
    line-height: 1.1;
    white-space: nowrap;
  }
  .brand-title {
    font-size: 35px;
    letter-spacing: -1px;
    line-height: 1.05;
    white-space: nowrap;
  }
  .brand-service {
    display: flex; align-items: center; gap: 8px;
    font-size: 24px;
    letter-spacing: 12px;
    text-transform: uppercase;
    line-height: 1;
  }
  .brand-service::before,
  .brand-service::after {
    content: "";
    height: 2px;
    background: var(--navy);
    flex: 0 0 42px;
  }
  .brand-service::after { flex: 1 1 auto; margin-left: -8px; }
  .contact-list {
    position: absolute;
    left: 31px; top: 202px;
    list-style: none;
  }
  .contact-item {
    display: flex; align-items: center; gap: 10px;
    height: 34px;
    margin-bottom: 13px;
    font-weight: 700;
    font-size: 19px;
    white-space: nowrap;
  }
  .contact-icon {
    width: 33px; height: 33px;
    border-radius: 5px;
    background: var(--soft-blue);
    display: flex; align-items: center; justify-content: center;
  }
  .contact-icon svg { width: 20px; height: 20px; fill: var(--navy); }
</style>
</head>
<body>
  <section class="billboard">
    <div class="pool-photo" role="img" aria-label="Photo of two smiling children playing with a beach ball in a bright blue swimming pool"></div>
    <div class="photo-fade"></div>
    <div class="frame"></div>

    <div class="brand">
      <div class="brand-mark"></div>
      <div class="brand-name">
        <div class="brand-owners">RUSTY &amp; CALDER PEMBROOK</div>
        <div class="brand-title">RUSTY’S POOLS</div>
        <div class="brand-service">&amp; Service</div>
      </div>
    </div>

    <ul class="contact-list">
      <li class="contact-item">
        <span class="contact-icon">
          <svg viewBox="0 0 24 24"><path d="M12 2a7 7 0 0 0-7 7c0 5 7 13 7 13s7-8 7-13a7 7 0 0 0-7-7zm0 9.5A2.5 2.5 0 1 1 12 6.5a2.5 2.5 0 0 1 0 5z"/></svg>
        </span>
        2716 Harlan Rd Millbrook,GA 31590
      </li>
      <li class="contact-item">
        <span class="contact-icon">
          <svg viewBox="0 0 24 24"><path d="M6.6 10.8a15 15 0 0 0 6.6 6.6l2.2-2.2a1 1 0 0 1 1-.25 11.4 11.4 0 0 0 3.6.57 1 1 0 0 1 1 1V20a1 1 0 0 1-1 1A17 17 0 0 1 3 4a1 1 0 0 1 1-1h3.5a1 1 0 0 1 1 1c0 1.25.2 2.45.57 3.57a1 1 0 0 1-.25 1z"/></svg>
        </span>
        555-014-2286
      </li>
      <li class="contact-item">
        <span class="contact-icon">
          <svg viewBox="0 0 24 24"><path d="M3 5h18a1 1 0 0 1 1 1v12a1 1 0 0 1-1 1H3a1 1 0 0 1-1-1V6a1 1 0 0 1 1-1zm1.5 2 7.5 5.5L19.5 7zm-.5 2v8l5-4zm16 0-5 4 5 4zm-9.4 5.3L5 18h14l-5.6-3.7L12 15.4z"/></svg>
        </span>
        rusty@rcpools.net
      </li>
    </ul>
  </section>
</body>
</html>
```